WP website design (Brenmoor)

We need a wordpress design for an established auction and real estate company based in Kentucky. The winning design will incorporate a professional color scheme with company logo in a clean layout with specified widgets. The design needs to consider that this will be developed on a responsive theme. Color is #307d84, with gray/black or other as an accent/highlight color.

Industry/Entity Type

Real Estate

Requirements
Must have
• Elelments of design need to consider that this site is going to be developed on a responsive theme.

Navigation:
1) Home 2) Current Auctions 3) Past Auctions 4) Meet the Staff 5) For Sellers 6) For Buyers 7) Testimonials 8) Contact Us

Colors will be the blue of logo plus black/gray or other accent color.

Slideshow will be prominent, please use stock real estate photo for initial image. Will have following in either header or sidebar: testimonials, social icons (FB, linkedin Twitter, RSS), Featured Auctions widget, newsletter signup form.

Footer will have contact info (below) and attached affiliation logos.
Brenmoor Auctions, Inc.
8415 Tamsen Rd., Brookvale ST 00000
glen.office@brenmoorbid.example
Phone: (555) 736 2048

```html
<!DOCTYPE html>
<html lang="en">
<head>
<meta charset="utf-8">
<title>Brenmoor Auctions, Inc.</title>
<link href="https://fonts.googleapis.com/css2?family=Open+Sans:wght@400;600;700&display=swap" rel="stylesheet">
<style>
:root{
  --teal:#307d84;
  --gold:#f2b705;
  --orange:#f0a22a;
  --ink:#222;
  --text:#666;
  --line:#ddd;
  --panel:#e6e6e6;
  --red:#d8262b;
}
*{box-sizing:border-box;margin:0;padding:0}
html,body{width:738px;height:1200px;overflow:hidden;background:#fff;font-family:"Open Sans",sans-serif;color:var(--text)}
.page{position:relative;width:738px;height:1200px}

.main-nav{height:30px;background:var(--gold);display:flex;align-items:center;padding-left:20px}
.main-nav a{font-size:10.5px;font-weight:700;color:var(--ink);text-decoration:none;text-transform:uppercase;padding:0 11px;border-right:1px solid rgba(0,0,0,.25);line-height:14px}
.main-nav a:first-child{padding-left:0}
.main-nav a:last-child{border-right:none}

.hero{position:relative;height:328px;background:linear-gradient(180deg,#cfe0ee 0%,#e4ecf2 30%,#9a7e64 55%,#6f6a52 78%,#4b5a33 100%)}
.brand{position:absolute;left:302px;top:8px;width:200px;height:72px;background:rgba(255,255,255,.92);display:flex;align-items:center;justify-content:center;gap:8px}
.brand-mark{width:16px;height:16px;background:var(--teal)}
.brand-name{color:var(--teal);font-weight:700;font-size:17px;line-height:1.1}
.search{position:absolute;right:28px;top:12px}
.slide-arrow{position:absolute;top:145px}
.slide-arrow.prev{left:8px}
.slide-arrow.next{right:8px}

.section-title{font-size:13px;font-weight:700;color:var(--ink);text-transform:uppercase;letter-spacing:.3px}
.projects{padding:18px 20px 14px;border-bottom:1px solid var(--line)}
.project-grid{display:grid;grid-template-columns:repeat(4,155px);gap:26px;margin-top:10px}
.project-photo{height:104px}
.project h3{margin-top:12px;font-size:11px;font-weight:400;color:var(--orange);text-transform:uppercase;line-height:15px}
.project p{margin-top:7px;font-size:11px;line-height:15px}
.more{display:block;margin-top:12px;font-size:10px;color:var(--ink);text-decoration:none}
.projects .more{margin-top:24px}

.widgets{display:grid;grid-template-columns:214px 222px 226px;gap:24px;padding:40px 20px 0}
.widget > .section-title{padding-bottom:9px;border-bottom:1px solid var(--line);margin-bottom:10px}
.welcome h3{font-size:11px;font-weight:400;color:var(--orange);text-transform:uppercase;line-height:15px}
.welcome p{margin-top:10px;font-size:11px;line-height:16px}
.welcome .hl{color:var(--orange)}
.news-item{display:flex;gap:10px;margin-bottom:12px}
.news-date{width:32px;flex:none;text-align:center;color:var(--ink)}
.news-date b{display:block;font-size:22px;font-weight:400;line-height:24px}
.news-date span{font-size:10px}
.news-item h4{font-size:11px;font-weight:400;color:var(--orange);line-height:15px}
.news-item p{font-size:11px;line-height:15px;margin-top:5px}
.subscribe{background:var(--panel);height:86px;padding:14px 10px}
.subscribe label{font-size:10px;font-weight:700;color:var(--ink);text-transform:uppercase}
.subscribe-row{display:flex;margin-top:8px}
.subscribe-row input{width:148px;height:22px;border:1px solid #ccc;font:10px "Open Sans",sans-serif;padding:0 6px}
.subscribe-row button{height:22px;padding:0 10px;background:var(--red);border:none;color:#fff;font:600 10px "Open Sans",sans-serif}
.clients-head{display:flex;justify-content:space-between;align-items:center;margin-top:16px;padding-bottom:9px;border-bottom:1px solid var(--line)}
.clients-row{display:flex;gap:14px;margin-top:14px;align-items:center}
.badge{width:44px;height:50px;background:#333}
.badge.round{border-radius:6px;background:#1e4e8c}
.badge.square{background:#111}

.site-footer{position:absolute;left:0;top:985px;width:738px;height:215px;background:linear-gradient(180deg,#3a4a58 0%,#22303b 55%,#141c22 100%);color:#fff;text-align:center}
.location{display:flex;justify-content:center;align-items:center;gap:8px;margin-top:22px}
.location h2{font-size:20px;font-weight:700;text-transform:uppercase;letter-spacing:.5px}
.address{margin-top:8px;font-size:10.5px;line-height:16px;text-transform:uppercase}
.social{display:flex;justify-content:center;gap:6px;margin-top:22px}
.social span{width:26px;height:26px;background:#f2f2f2}
.copyright{margin-top:10px;font-size:10px}
</style>
</head>
<body>
<div class="page">
  <nav class="main-nav">
    <a href="#">Current Auctions</a><a href="#">Past Auctions</a><a href="#">Meet the Staff</a><a href="#">For Sellers</a><a href="#">For Buyers</a><a href="#">Testimonials</a><a href="#">Contact Us</a>
  </nav>

  <header class="hero" role="img" aria-label="Slideshow photo of a two-storey brick family house with a lawn">
    <div class="brand"><span class="brand-mark"></span><span class="brand-name">Brenmoor<br>Auctions Inc.</span></div>
    <svg class="search" width="30" height="30" viewBox="0 0 30 30"><circle cx="15" cy="15" r="15" fill="#555"/><circle cx="13" cy="13" r="5.5" fill="none" stroke="#fff" stroke-width="2"/><line x1="17" y1="17" x2="22" y2="22" stroke="#fff" stroke-width="2.5"/></svg>
    <svg class="slide-arrow prev" width="14" height="30" viewBox="0 0 14 30"><polyline points="12,2 2,15 12,28" fill="none" stroke="#fff" stroke-width="2.5"/></svg>
    <svg class="slide-arrow next" width="14" height="30" viewBox="0 0 14 30"><polyline points="2,2 12,15 2,28" fill="none" stroke="#fff" stroke-width="2.5"/></svg>
  </header>

  <section class="projects">
    <h2 class="section-title">Latest Projects</h2>
    <div class="project-grid">
      <article class="project">
        <div class="project-photo" role="img" aria-label="Garden path with lamp post and flowers" style="background:linear-gradient(160deg,#9cc07a,#4c7a3a)"></div>
        <h3>Lorem ipsum dolor sit amet, consec tetuer adipi</h3>
        <p>Vestibu lum molestie lacuilis. Aenean on ummy hendrerit.</p>
      </article>
      <article class="project">
        <div class="project-photo" role="img" aria-label="Red flower beds on a green lawn" style="background:linear-gradient(160deg,#6e9a4a,#c23a3a 60%,#5d8a3c)"></div>
        <h3>Amet, consec tetuer adipi praesent vestibu.</h3>
        <p>Lum molestie lacuilis. Aenean on ummy hendrerit.</p>
      </article>
      <article class="project">
        <div class="project-photo" role="img" aria-label="Garden pond with trees" style="background:linear-gradient(160deg,#b8d08a,#4f7d3c 60%,#2f5a36)"></div>
        <h3>Dolor sit amet, consec tetuer adipi praesent.</h3>
        <p>Vestibu lum molestie. Aenean on ummy hendrerit, Phasellus porta. Fusce suscip.</p>
      </article>
      <article class="project">
        <div class="project-photo" role="img" aria-label="Sunlit park with tall trees" style="background:linear-gradient(160deg,#e6e2a0,#8aa84e 50%,#3e6a2e)"></div>
        <h3>Consec tetuer adipi raese nt vestibulum molestie.</h3>
        <p>On ummy hendrerit. Phasellus porta. Fusce suscipit vari.</p>
      </article>
    </div>
    <a class="more" href="#">more projects</a>
  </section>

  <section class="widgets">
    <div class="widget welcome">
      <h2 class="section-title">Welcome!</h2>
      <h3>Lorem ipsum dolor sit amet, consec</h3>
      <p>Vestibu lum molestie lacuilis. Aenean on ummy hendrerit. <span class="hl">Phasellus porta. Fusce</span> suscipit varius mum socis sodales et.</p>
      <p>Vestibu lum molestie lacuilis. Aenean on ummy hendrerit. Phasellus porta. Fusce</p>
      <a class="more" href="#">more info</a>
    </div>
    <div class="widget news">
      <h2 class="section-title">Latest News</h2>
      <div class="news-item">
        <div class="news-date"><b>20</b><span>may</span></div>
        <div><h4>Lorem ipsum dolor sit amet, consec tetuer</h4><p>Vestibu lum molestie lacuilis. Aenean on ummy hendrerit, Phasellus</p></div>
      </div>
      <div class="news-item">
        <div class="news-date"><b>15</b><span>may</span></div>
        <div><h4>Adipi praesent vestibu lum molestie lacuilis.</h4></div>
      </div>
      <a class="more" href="#">more news</a>
    </div>
    <div class="widget">
      <h2 class="section-title">Subscribe Newsletter</h2>
      <form class="subscribe">
        <label>Subscribe Email</label>
        <div class="subscribe-row"><input type="text" placeholder="enter email address"><button type="button">Submit</button></div>
      </form>
      <div class="clients-head">
        <h2 class="section-title">Our Clients</h2>
        <svg width="22" height="10" viewBox="0 0 22 10"><polyline points="6,1 2,5 6,9" fill="none" stroke="#333" stroke-width="1.5"/><polyline points="16,1 20,5 16,9" fill="none" stroke="#333" stroke-width="1.5"/></svg>
      </div>
      <div class="clients-row">
        <span class="badge round"></span>
        <span class="badge"></span>
        <span class="badge square"></span>
      </div>
    </div>
  </section>

  <footer class="site-footer" role="img" aria-label="Night city skyline behind the contact details">
    <div class="location">
      <svg width="16" height="22" viewBox="0 0 16 22"><path d="M8 0C3.6 0 0 3.4 0 7.8 0 13 8 22 8 22s8-9 8-14.2C16 3.4 12.4 0 8 0z" fill="var(--teal)"/><circle cx="8" cy="8" r="3" fill="#fff"/></svg>
      <h2>Our Location</h2>
    </div>
    <p class="address">Brenmoor Auctions, Inc.<br>8415 Tamsen Rd.,<br>Brookvale ST 00000<br>glen.office@brenmoorbid.example<br>Phone: (555) 736 2048</p>
    <div class="social"><span></span><span></span><span></span><span></span></div>
    <p class="copyright">2014 © Privacy policy</p>
  </footer>
</div>
</body>
</html>
```